Business cards to launch an education platform

Hi,
I am looking at having new business cards designed.
I am a startup, developing a web platform for schools and university, the education world. It's an online assessment system.
I would like a card that looks classy, and that is using the colors and the font of my logo.

I have attached:
1) my logo
2) A business card that I have designed quickly so you can have all the information required in the card, but I really don't like it.
3) The font that I am using (Lato Regular) to design my web platform
4) Some screenshots of my web platform so you can have a look at the style that I have.

Target Market(s)

Major market: Education system: Schools and university
Minor markets: Business in general

Industry/Entity Type

Business

Contact Information for Business Card

Tessa Vinall
Director

M: 0487 312 950
E: tessa.vinall@copperLoomVentures.com.au

Requirements
Must have
• The colors of my logo

```html
<!DOCTYPE html>
<html lang="en">
<head>
<meta charset="utf-8">
<title>Copper Loom Ventures – Business Card</title>
<link href="https://fonts.googleapis.com/css2?family=Lato:wght@400;700&display=swap" rel="stylesheet">
<style>
  :root {
    --page-bg: #e8e5e1;
    --card-light: #f3f3f4;
    --card-mid: #dfe1e5;
    --navy-deep: #163f6f;
    --navy: #1f5390;
    --navy-soft: #2d68a8;
    --ink: #1f3a5c;
    --teal: #2f8d9c;
    --text: #2d3440;
  }
  html, body {
    margin: 0;
    width: 1200px;
    height: 970px;
    overflow: hidden;
    background: var(--page-bg);
  }
  .canvas {
    position: relative;
    width: 1200px;
    height: 970px;
  }
  .business-card {
    position: absolute;
    left: 80px;
    top: 189px;
    width: 1040px;
    height: 592px;
    overflow: hidden;
    background: linear-gradient(160deg, var(--card-light), var(--card-mid));
    box-shadow: 0 18px 40px rgba(0,0,0,0.18);
    font-family: "Lato", sans-serif;
  }
  .card-waves {
    position: absolute;
    inset: 0;
  }
  .brand {
    position: absolute;
    right: 55px;
    top: 118px;
    display: flex;
    align-items: center;
    gap: 22px;
  }
  .brand-square {
    width: 86px;
    height: 86px;
    background: var(--navy-deep);
  }
  .brand-name {
    font-size: 38px;
    font-weight: 400;
    letter-spacing: 2px;
    color: var(--ink);
  }
  .person {
    position: absolute;
    left: 55px;
    top: 308px;
  }
  .person-name {
    margin: 0;
    font-size: 39px;
    font-weight: 400;
    color: var(--ink);
    line-height: 1;
  }
  .person-role {
    margin: 2px 0 0;
    font-size: 26px;
    color: var(--teal);
    line-height: 1.1;
  }
  .contact {
    position: absolute;
    left: 55px;
    top: 412px;
    margin: 0;
    padding: 0;
    list-style: none;
  }
  .contact-item {
    display: flex;
    align-items: center;
    gap: 12px;
    height: 40px;
    font-size: 27px;
    color: var(--text);
  }
  .contact-icon {
    width: 32px;
    height: 32px;
    flex: none;
  }
</style>
</head>
<body>
<main class="canvas">
  <section class="business-card">
    <svg class="card-waves" viewBox="0 0 1040 592" preserveAspectRatio="none" aria-hidden="true">
      <path d="M0,0 H1040 V6 C820,0 330,40 0,225 Z" fill="var(--navy)"/>
      <path d="M1040,230 C920,420 520,520 0,560 V592 H1040 Z" fill="var(--navy-soft)"/>
      <path d="M1040,300 C900,460 560,540 0,565 V592 H1040 Z" fill="var(--navy-deep)"/>
    </svg>

    <div class="brand">
      <div class="brand-square"></div>
      <div class="brand-name">Copper Loom Ventures</div>
    </div>

    <div class="person">
      <h1 class="person-name">Tessa Vinall</h1>
      <p class="person-role">Director</p>
    </div>

    <ul class="contact">
      <li class="contact-item">
        <svg class="contact-icon" viewBox="0 0 32 32" aria-hidden="true">
          <rect width="32" height="32" fill="var(--teal)"/>
          <rect x="11" y="5" width="10" height="22" rx="2" fill="none" stroke="#fff" stroke-width="2"/>
          <rect x="13" y="8" width="6" height="6" fill="#fff"/>
        </svg>
        <span>0487 312 950</span>
      </li>
      <li class="contact-item">
        <svg class="contact-icon" viewBox="0 0 32 32" aria-hidden="true">
          <rect width="32" height="32" fill="var(--teal)"/>
          <rect x="6" y="9" width="20" height="14" fill="none" stroke="#fff" stroke-width="2"/>
          <path d="M6,9 L16,17 L26,9" fill="none" stroke="#fff" stroke-width="2"/>
        </svg>
        <span>tessa.vinall@copperLoomVentures.com.au</span>
      </li>
    </ul>
  </section>
</main>
</body>
</html>
```